Private Gym Needs a Rack Card Design

We need a basic front and back rack card (same size as post card) that gives basic information about our brand, and includes our logo. Please see attached logo and required content below.

Target Market(s)

Upscale, private gym.

Industry/Entity Type

Gym

Font styles to use
Sans Serif

Colors
ffffff
5c5c5c
000000
dbdbdb
f78f20

Requirements
Must have
• Business Logo and the following text in a clean, modern, easy-to-read, artistic manner. Style and design must be clean, incorporate our color scheme of MOSTLY white, light grey, charcoal, with just pops of orange. We want the card itself to be mostly white background. Must include website URL as well: corevaultfitness.com
• FRONT CARD:
• Logo
• A safe and individualized approach to exercise
• our path employs the latest weight resistance training exercises and coaching for healthy living. Not only is our workout methodology effective, it’s safe.
• Our Path…
• -Improves Functional Movement
• -Promotes Weight Loss
• -Builds Strength
• -Increases Flexibility 

• BACK:
• Change Your Body. Find Your Strength.
• There’s 40 years of success behind our proven method
• What is Iron Path? 
• Iron Path is all about teaching our clients how to lift weights and exercise with the proper technique. There’s no slinging or jerking at our gym; only controlled movements that yield real results.
• Come workout with us in our private gym. We are located in Durham adjacent to Larch Campus and 5 minutes from downtown Durham.
• Address: 482 Fenwick Ave, Durham, NC 27705
• Phone: (919) 555-0147
• Hours: 9:00 AM – 9:00 PM
Nice to have
• Great organization of text, maybe some columns, colored bullet points, cool graphics and logos.
Should not have
• Busy or crowded design. All lines should be sleek, straight, and streamline. NO STOCK IMAGES, but logos are GREAT

```html
<!DOCTYPE html>
<html lang="en">
<head>
<meta charset="utf-8">
<title>Iron Path Rack Card</title>
<link rel="stylesheet" href="https://fonts.googleapis.com/css2?family=Open+Sans:wght@300;400;600;700&family=Roboto+Condensed:wght@700&family=Dancing+Script:wght@500&display=swap">
<style>
  :root {
    --white: #ffffff;
    --charcoal: #5c5c5c;
    --black: #000000;
    --light-grey: #dbdbdb;
    --orange: #f26f2f;
    --orange-strip: #f78f20;
    --stage: #ececec;
  }
  * { box-sizing: border-box; margin: 0; padding: 0; }
  html, body { width: 1200px; height: 1155px; overflow: hidden; }
  body { background: var(--stage); position: relative; font-family: "Open Sans", sans-serif; color: var(--charcoal); }

  .card {
    position: absolute; top: 122px; width: 449px; height: 950px;
    background: var(--white); overflow: hidden;
    box-shadow: 0 2px 8px rgba(0,0,0,.18);
  }
  .card--front { left: 138px; }
  .card--back { left: 624px; }
  .abs { position: absolute; }

  /* front */
  .brand { left: 0; right: 0; top: 26px; text-align: center; }
  .brand__name { font-family: "Open Sans", sans-serif; font-weight: 700; font-size: 50px; line-height: 1; color: var(--charcoal); letter-spacing: 1px; text-transform: uppercase; }
  .brand__tag { margin-top: 12px; font-size: 12px; font-weight: 600; letter-spacing: 4.2px; color: var(--charcoal); }

  .photo { background: radial-gradient(ellipse at 55% 45%, #e9d2c2 0%, #f1ebe6 35%, #f6f6f6 70%); }
  .photo--front { left: 0; top: 118px; width: 449px; height: 325px; }

  .band { left: 0; width: 449px; top: 443px; height: 170px; background: var(--orange); }
  .band::after { content: ""; position: absolute; left: 0; right: 0; bottom: 0; height: 8px; background: var(--orange-strip); }

  .front-headline { left: 0; right: 0; top: 464px; text-align: center; font-family: "Roboto Condensed", sans-serif; font-weight: 700; font-size: 35px; line-height: 42px; color: var(--white); text-shadow: 0 2px 3px rgba(0,0,0,.25); }
  .front-url { left: 0; right: 0; top: 566px; text-align: center; font-size: 26px; color: var(--white); letter-spacing: .3px; }

  .front-intro { left: 27px; width: 392px; top: 640px; font-size: 15px; line-height: 26px; text-align: justify; }
  .path-title { left: 27px; top: 744px; font-size: 28px; font-weight: 700; color: var(--orange); }
  .benefits { left: 27px; top: 794px; list-style: none; }
  .benefits li { display: flex; align-items: center; gap: 12px; font-size: 22px; font-weight: 600; height: 35px; }
  .benefits svg { width: 20px; height: 20px; flex: none; }

  /* back */
  .back-headline { left: 30px; top: 30px; font-family: "Roboto Condensed", sans-serif; font-weight: 700; font-size: 47px; line-height: 56px; color: var(--orange); }
  .what-title { left: 30px; top: 174px; font-size: 25px; font-weight: 700; color: var(--charcoal); }
  .what-text { left: 30px; width: 380px; top: 218px; font-size: 13px; line-height: 21px; text-align: justify; color: #222; }
  .legacy { left: 30px; top: 332px; font-size: 22px; line-height: 29px; font-weight: 300; color: var(--charcoal); }

  .band--back { z-index: 1; }
  .hours { left: 0; width: 196px; top: 460px; text-align: center; z-index: 2; font-family: "Roboto Condensed", sans-serif; font-weight: 700; color: var(--white); font-size: 30px; line-height: 40px; text-shadow: 0 2px 3px rgba(0,0,0,.25); }
  .hours .dash { line-height: 14px; display: block; }

  .photo--people { left: 238px; top: 312px; width: 200px; height: 495px; z-index: 3; background: linear-gradient(180deg, #e4b89c 0%, #d9a688 40%, #6b6b6b 62%, #d9a688 80%, #e9887c 100%); opacity: .92; border-radius: 40px 40px 10px 10px; }
  .visit-text { left: 30px; width: 194px; top: 624px; font-size: 12px; line-height: 17px; color: var(--charcoal); }
  .photo--dumbbells { left: 30px; top: 718px; width: 150px; height: 70px; background: radial-gradient(ellipse at center, #b8b8b8 0%, #dedede 55%, #ffffff 90%); }

  .contact-label { left: 30px; top: 796px; font-family: "Dancing Script", cursive; font-weight: 500; font-size: 34px; color: var(--charcoal); }
  .contact-phone { left: 30px; top: 842px; font-family: "Roboto Condensed", sans-serif; font-weight: 700; font-size: 47px; color: var(--orange); }
  .contact-address { left: 30px; top: 900px; font-size: 22px; font-weight: 600; color: var(--charcoal); white-space: nowrap; }
</style>
</head>
<body>

<section class="card card--front">
  <div class="abs brand">
    <div class="brand__name">Iron Path</div>
    <div class="brand__tag">PRIVATE TRAINING STUDIO</div>
  </div>
  <div class="abs photo photo--front" role="img" aria-label="Photo of a smiling woman in workout clothes doing a push-up"></div>
  <div class="abs band"></div>
  <h1 class="abs front-headline">A safe and individualized<br>approach to exercise</h1>
  <div class="abs front-url">www.corevaultfitness.com</div>
  <p class="abs front-intro">Our path employs the latest weight resistance training exercises and coaching for healthy living. Not only is our workout methodology effective, it’s safe.</p>
  <h2 class="abs path-title">Our Path…</h2>
  <ul class="abs benefits">
    <li><svg viewBox="0 0 20 20"><rect x="1.5" y="3.5" width="15" height="15" fill="none" stroke="#5c5c5c" stroke-width="2"/><path d="M5 10l4 4 9-12" fill="none" stroke="#f26f2f" stroke-width="3"/></svg>Improves Functional Movement</li>
    <li><svg viewBox="0 0 20 20"><rect x="1.5" y="3.5" width="15" height="15" fill="none" stroke="#5c5c5c" stroke-width="2"/><path d="M5 10l4 4 9-12" fill="none" stroke="#f26f2f" stroke-width="3"/></svg>Promotes Weight Loss</li>
    <li><svg viewBox="0 0 20 20"><rect x="1.5" y="3.5" width="15" height="15" fill="none" stroke="#5c5c5c" stroke-width="2"/><path d="M5 10l4 4 9-12" fill="none" stroke="#f26f2f" stroke-width="3"/></svg>Builds Strength</li>
    <li><svg viewBox="0 0 20 20"><rect x="1.5" y="3.5" width="15" height="15" fill="none" stroke="#5c5c5c" stroke-width="2"/><path d="M5 10l4 4 9-12" fill="none" stroke="#f26f2f" stroke-width="3"/></svg>Increases Flexibility</li>
  </ul>
</section>

<section class="card card--back">
  <h1 class="abs back-headline">Change Your Body<br>Find Your Strength</h1>
  <h2 class="abs what-title">What is Iron Path?</h2>
  <p class="abs what-text">Iron Path is all about teaching our clients how to lift weights and exercise with the proper technique. There’s no slinging or jerking at our gym; only controlled movements that yield real results.</p>
  <p class="abs legacy">There’s 40 Years Of<br>Success Behind Our<br>Proven Method</p>
  <div class="abs band band--back"></div>
  <div class="abs hours">hours:<br>9:00 AM<span class="dash">-</span>9:00 PM</div>
  <div class="abs photo--people" role="img" aria-label="Photo of a fit man and woman standing together holding a measuring tape"></div>
  <p class="abs visit-text">Come workout with us in our private gym. We are located in Durham adjacent to Larch Campus and 5 minutes from downtown Durham.</p>
  <div class="abs photo--dumbbells" role="img" aria-label="Photo of a pair of chrome dumbbells"></div>
  <div class="abs contact-label">Contact Us</div>
  <div class="abs contact-phone">(919) 555-0147</div>
  <div class="abs contact-address">482 Fenwick Ave, Durham, NC 27705</div>
</section>

</body>
</html>
```